Private Investigation Business Card Design

I need a business card for a new private investigation company named Brisk Lens Inquiries. I perform mainly surveillance jobs, vehicle repossessions, document serves etc. The final design should aim for a professional look. The logo has a magnifying glass with stick man arms and legs and is in a running action to show the "BRISK" aspect of the name. If the colour scheme could remain the same as the website www.brisklensinquiries.example.au with silvers,blacks and a couple electric blue highlights.
Industry/Entity Type
Business
Contact Information for Business Card
Morgan Kilbride
Brisk Lens Inquiries
0438276104
PO Box 58, Fernvale NSW 2291
info@brisklensinquiries.example.au
www.brisklensinquiries.example.au
Look and feel
Each slider illustrates characteristics of the customer's brand and the style your logo design should communicate.

```html
<!DOCTYPE html>
<html lang="en">
<head>
<meta charset="utf-8">
<title>Brisk Lens Inquiries – Business Card</title>
<link rel="stylesheet" href="https://fonts.googleapis.com/css2?family=Open+Sans:wght@400;700;800&display=swap">
<style>
  :root {
    --page-bg: #e7e5e2;
    --card-white: #ffffff;
    --card-black: #2a2a2a;
    --ink-dark: #1f1f1f;
    --ink-grey: #8a8a8a;
    --band-black: #1c1c1c;
    --band-grey: #8d8c92;
    --band-light: #c9c9cc;
    --logo-silver: #9a9a9e;
    --logo-white: #f2f2f2;
    --line-faint: rgba(255,255,255,0.035);
  }
  * { margin: 0; padding: 0; box-sizing: border-box; }
  html, body { width: 1200px; height: 900px; overflow: hidden; }
  body {
    background: var(--page-bg);
    font-family: "Open Sans", Arial, sans-serif;
    display: flex;
    flex-direction: column;
    align-items: center;
    justify-content: center;
    gap: 48px;
  }
  .card {
    position: relative;
    width: 650px;
    height: 372px;
    overflow: hidden;
    box-shadow: 0 6px 18px rgba(0,0,0,0.18);
  }

  /* Back side */
  .card-back {
    background:
      repeating-linear-gradient(0deg, var(--line-faint) 0 1px, transparent 1px 3px),
      var(--card-black);
  }
  .card-back .wordmark {
    position: absolute;
    left: 0; right: 0; top: 150px;
    text-align: center;
    color: var(--logo-white);
  }

  .wordmark .brand-main {
    display: block;
    font-weight: 800;
    font-size: 64px;
    line-height: 1;
    letter-spacing: 2px;
  }
  .wordmark .brand-sub {
    display: block;
    font-weight: 800;
    font-size: 22px;
    letter-spacing: 6px;
    margin-top: 4px;
  }

  /* Front side */
  .card-front { background: var(--card-white); }
  .card-front .bands { position: absolute; inset: 0; }
  .holder {
    position: absolute;
    left: 78px; top: 22px;
  }
  .holder .holder-name {
    font-weight: 700;
    font-size: 17px;
    color: var(--ink-dark);
  }
  .holder .holder-company {
    font-size: 14px;
    color: var(--ink-grey);
    margin-top: -3px;
  }
  .contact {
    position: absolute;
    left: 34px; top: 136px;
    font-size: 14px;
    color: var(--ink-grey);
    line-height: 1.45;
    list-style: none;
  }
  .contact .address { margin-bottom: 8px; color: #a3a3a3; }
  .contact li { display: flex; align-items: center; gap: 7px; }
  .contact svg { width: 11px; height: 11px; fill: var(--ink-dark); flex: none; }
  .card-front .wordmark {
    position: absolute;
    left: 290px; top: 150px;
    color: var(--logo-silver);
    display: flex;
    align-items: center;
    gap: 18px;
  }
  .card-front .wordmark .brand-main { font-size: 56px; }
  .card-front .wordmark .brand-sub { font-size: 19px; letter-spacing: 5px; }
  .brand-dot {
    width: 20px; height: 20px;
    border-radius: 50%;
    background: var(--logo-silver);
    flex: none;
  }
</style>
</head>
<body>

  <section class="card card-back" aria-label="Card back">
    <div class="wordmark">
      <span class="brand-main">BRISK</span>
      <span class="brand-sub">LENS INQUIRIES</span>
    </div>
  </section>

  <section class="card card-front" aria-label="Card front">
    <svg class="bands" viewBox="0 0 650 372" preserveAspectRatio="none" aria-hidden="true">
      <polygon points="0,0 62,0 38,38 0,38" fill="var(--band-light)"/>
      <polygon points="46,0 62,0 38,38 26,38" fill="var(--band-black)"/>
      <polygon points="0,278 320,278 300,300 0,300" fill="var(--band-black)"/>
      <polygon points="300,300 320,278 330,278 312,300" fill="var(--band-light)"/>
      <polygon points="330,300 348,280 650,280 650,372 330,372" fill="var(--band-grey)"/>
    </svg>

    <div class="holder">
      <p class="holder-name">Morgan Kilbride</p>
      <p class="holder-company">Brisk Lens Inquiries</p>
    </div>

    <ul class="contact">
      <li class="address">PO Box 58, Fernvale<br>NSW 2291</li>
      <li>
        <svg viewBox="0 0 12 12"><path d="M2 2h2l1 2.5-1.2 1a6 6 0 0 0 2.7 2.7l1-1.2L10 8v2a1 1 0 0 1-1 1A8 8 0 0 1 1 3a1 1 0 0 1 1-1z"/></svg>
        0438276104
      </li>
      <li>
        <svg viewBox="0 0 12 12"><path d="M1 3h10v6H1zM1.6 3.4 6 6.6l4.4-3.2" stroke="#fff" stroke-width="0.8"/></svg>
        info@brisklensinquiries.example.au
      </li>
      <li>
        <svg viewBox="0 0 12 12"><path d="M5 7 7 5M4 6 2.5 7.5a1.4 1.4 0 0 0 2 2L6 8M8 6l1.5-1.5a1.4 1.4 0 0 0-2-2L6 4" fill="none" stroke="var(--ink-dark)" stroke-width="1.2"/></svg>
        www.brisklensinquiries.example.au
      </li>
    </ul>

    <div class="wordmark">
      <div>
        <span class="brand-main">BRISK</span>
        <span class="brand-sub">LENS INQUIRIES</span>
      </div>
      <span class="brand-dot" aria-hidden="true"></span>
    </div>
  </section>

</body>
</html>
```